Business card design for a engineering company

I need a double sided business card design for my company "Velbrook Stream Systems". The card will be used in Malaysia. Sleek and professional, with a little design flare to it.
Information to showcase:
1. Company logo
2. Name, title, phone, email address, website address
3. our products "Pumping technology, Valve & actuation, Air Moving Technology
Example:
Mark Dovan
Business manager
mark.dovan@velbrook-example.com
www.velbrook-example.com.my
- Pumping technology
- Valve & actuation
- Air moving technology
Target Market(s)
engineers, purchasing managers
Industry/Entity Type
Business
Contact Information for Business Card
Mark Dovan
Business manager
mark.dovan@velbrook-example.com
www.velbrook-example.com.my
- Pumping technology
- Valve & actuation
- Air moving technology
catch phrase : "Solving flow challenges, exceeding expectations"

```html
<!DOCTYPE html>
<html lang="en">
<head>
<meta charset="utf-8">
<title>Velbrook Stream Systems – Business Card</title>
<link rel="stylesheet" href="https://fonts.googleapis.com/css2?family=Arimo:wght@400;700&display=swap">
<style>
  :root {
    --teal: #1f4f63;
    --teal-deep: #163c4c;
    --yellow: #f2c40f;
    --orange: #e8a23a;
    --ink: #1f4f63;
    --paper: #ffffff;
    --paper-shade: #f1f2f2;
    --backdrop: #e9e6e1;
    --grey: #9aa7ad;
  }
  * { box-sizing: border-box; margin: 0; padding: 0; }
  html, body { width: 1200px; height: 1023px; overflow: hidden; }
  body {
    background: var(--backdrop);
    font-family: "Arimo", Arial, sans-serif;
    position: relative;
  }
  .card {
    position: absolute;
    width: 580px;
    height: 330px;
    border-radius: 16px;
    overflow: hidden;
    background: linear-gradient(135deg, var(--paper) 0%, var(--paper-shade) 100%);
    box-shadow: 0 10px 30px rgba(0,0,0,0.18);
  }
  .card-front { left: 70px; top: 110px; }
  .card-back { left: 550px; top: 580px; }

  /* brand lockup */
  .brand { display: flex; align-items: center; gap: 14px; color: var(--ink); font-weight: 700; }
  .brand-mark { background: var(--teal); flex: none; }
  .card-front .brand {
    position: absolute; left: 0; right: 0; top: 108px; justify-content: center;
  }
  .card-front .brand-mark { width: 46px; height: 46px; }
  .card-front .brand-name { font-size: 34px; letter-spacing: 1px; }

  .front-band {
    position: absolute; left: 0; right: 0; bottom: 0; height: 62px;
    background: var(--teal);
    display: flex; align-items: center; justify-content: center;
  }
  .catchphrase { color: var(--orange); font-size: 20px; letter-spacing: 0.5px; }

  /* back */
  .card-back .brand { position: absolute; left: 36px; top: 26px; }
  .card-back .brand-mark { width: 28px; height: 28px; }
  .card-back .brand-name { font-size: 21px; letter-spacing: 0.5px; }

  .products {
    position: absolute; left: 36px; top: 70px; list-style: none;
    color: var(--orange); font-size: 14px; line-height: 21px;
  }
  .products li::before {
    content: ""; display: inline-block; width: 6px; height: 6px;
    background: var(--orange); border-radius: 50%; margin-right: 9px; vertical-align: middle;
  }
  .back-swoosh { position: absolute; left: 0; top: 0; width: 580px; height: 330px; }

  .contact {
    position: absolute; right: 30px; bottom: 16px; text-align: right; color: #fff;
  }
  .contact-name { color: var(--yellow); font-size: 22px; font-weight: 400; line-height: 26px; }
  .contact-title { color: #fff; font-size: 14px; line-height: 17px; margin-bottom: 6px; }
  .contact-list { list-style: none; font-size: 13px; line-height: 18px; }
  .contact-list li { display: flex; align-items: center; justify-content: flex-end; gap: 8px; }
  .contact-list svg { width: 12px; height: 12px; flex: none; }
</style>
</head>
<body>

  <section class="card card-front" aria-label="Card front">
    <div class="brand">
      <span class="brand-mark"></span>
      <span class="brand-name">Velbrook Stream Systems</span>
    </div>
    <div class="front-band">
      <p class="catchphrase">Solving flow challenges, exceeding expectations</p>
    </div>
  </section>

  <section class="card card-back" aria-label="Card back">
    <svg class="back-swoosh" viewBox="0 0 580 330" aria-hidden="true">
      <defs>
        <linearGradient id="tealFill" x1="0" y1="0" x2="1" y2="1">
          <stop offset="0" stop-color="#2a6278"/>
          <stop offset="1" stop-color="#1a4558"/>
        </linearGradient>
      </defs>
      <path d="M0 160 C 200 115, 420 120, 580 160 L580 330 L0 330 Z" fill="#f2c40f"/>
      <path d="M0 167 C 200 122, 420 127, 580 167 L580 330 L0 330 Z" fill="#ffffff"/>
      <path d="M0 174 C 200 129, 420 134, 580 174 L580 330 L0 330 Z" fill="url(#tealFill)"/>
    </svg>

    <div class="brand">
      <span class="brand-mark"></span>
      <span class="brand-name">Velbrook Stream Systems</span>
    </div>

    <ul class="products">
      <li>Pumping technology</li>
      <li>Valve &amp; actuation</li>
      <li>Air moving technology</li>
    </ul>

    <div class="contact">
      <p class="contact-name">Mark Dovan</p>
      <p class="contact-title">Business manager</p>
      <ul class="contact-list">
        <li>Your Address
          <svg viewBox="0 0 12 12"><path d="M6 0a4 4 0 0 0-4 4c0 3 4 8 4 8s4-5 4-8a4 4 0 0 0-4-4zm0 5.5a1.5 1.5 0 1 1 0-3 1.5 1.5 0 0 1 0 3z" fill="#f2c40f"/></svg>
        </li>
        <li>+60 3 5550 4127
          <svg viewBox="0 0 12 12"><circle cx="6" cy="6" r="5" fill="none" stroke="#f2c40f" stroke-width="1.2"/><path d="M4 3.5l1 1-0.6 0.8c0.4 0.9 1 1.5 1.9 1.9l0.8-0.6 1 1-0.8 0.9C5.6 8.3 3.7 6.4 3.5 4.3z" fill="#f2c40f"/></svg>
        </li>
        <li>mark.dovan@velbrook-example.com
          <svg viewBox="0 0 12 12"><rect x="0.6" y="2.5" width="10.8" height="7" fill="none" stroke="#f2c40f" stroke-width="1.2"/><path d="M0.6 2.5L6 6.5l5.4-4" fill="none" stroke="#f2c40f" stroke-width="1.2"/></svg>
        </li>
        <li>www.velbrook-example.com.my
          <svg viewBox="0 0 12 12"><circle cx="6" cy="6" r="5.2" fill="none" stroke="#f2c40f" stroke-width="1.1"/><ellipse cx="6" cy="6" rx="2.2" ry="5.2" fill="none" stroke="#f2c40f" stroke-width="1"/><path d="M0.8 6h10.4" stroke="#f2c40f" stroke-width="1"/></svg>
        </li>
      </ul>
    </div>
  </section>

</body>
</html>
```